Marrowfield Benefit Advisors Business Card Design

I already placed order for cards through sketch hive.

Double sided- back Navy with White logo and raised silver "swoosh"

```html
<!DOCTYPE html>
<html lang="en">
<head>
<meta charset="UTF-8">
<title>Marrowfield Benefit Advisors – Business Card</title>
<link href="https://fonts.googleapis.com/css2?family=Cinzel:wght@400;500&family=Poppins:wght@300;400&display=swap" rel="stylesheet">
<style>
  :root {
    --backdrop: #cfcfcf;
    --card: #f3f3f3;
    --ink: #a9a9a9;
    --ink-dark: #9c9c9c;
    --rule: #bdbdbd;
  }
  * { box-sizing: border-box; margin: 0; padding: 0; }
  html, body {
    width: 1093px; height: 1200px; overflow: hidden;
    background: var(--backdrop);
  }
  .canvas { position: relative; width: 1093px; height: 1200px; }
  .card {
    position: absolute; left: 190px; width: 712px;
    background: var(--card); overflow: hidden;
  }
  .card--front { top: 130px; height: 436px; }
  .card--back  { top: 636px; height: 441px; }

  .brand {
    position: absolute; left: 0; right: 0;
    display: flex; align-items: center; justify-content: center; gap: 14px;
    font-family: "Cinzel", serif; font-weight: 500; font-size: 29px;
    color: var(--ink); letter-spacing: 1px; white-space: nowrap;
  }
  .brand__dot { width: 14px; height: 14px; border-radius: 50%; background: var(--ink); }
  .card--front .brand { top: 110px; }
  .card--back .brand { top: 206px; }

  .person {
    position: absolute; right: 382px; top: 272px; text-align: right;
    white-space: nowrap;
  }
  .person__name {
    font-family: "Cinzel", serif; font-weight: 400; font-size: 27px;
    color: var(--ink); letter-spacing: 1px; line-height: 1.1;
  }
  .person__role {
    font-family: "Poppins", sans-serif; font-weight: 400; font-size: 19px;
    color: var(--ink); line-height: 1.2;
  }
  .divider {
    position: absolute; left: 357px; top: 260px; width: 1px; height: 75px;
    background: var(--rule);
  }
  .contacts {
    position: absolute; left: 385px; top: 258px; list-style: none;
    font-family: "Poppins", sans-serif; font-weight: 400; font-size: 20px;
    color: var(--ink-dark); white-space: nowrap;
  }
  .contacts li { display: flex; align-items: center; height: 26px; }
  .contacts svg { width: 18px; height: 18px; margin-right: 10px; flex: none; }
  .address {
    position: absolute; left: 0; right: 0; top: 374px; text-align: center;
    font-family: "Poppins", sans-serif; font-weight: 400; font-size: 19px;
    color: var(--ink); white-space: nowrap;
  }
</style>
</head>
<body>
<main class="canvas">
  <section class="card card--front">
    <div class="brand"><span class="brand__dot"></span>Marrowfield Benefit Advisors</div>

    <div class="person">
      <p class="person__name">DANIEL HARTLEY</p>
      <p class="person__role">Managing Director</p>
    </div>
    <div class="divider"></div>
    <ul class="contacts">
      <li>
        <svg viewBox="0 0 24 24" fill="none" stroke="#a9a9a9" stroke-width="1.8" stroke-linecap="round" stroke-linejoin="round"><path d="M22 16.9v3a2 2 0 0 1-2.2 2 19.8 19.8 0 0 1-8.6-3.1 19.5 19.5 0 0 1-6-6A19.8 19.8 0 0 1 2.1 4.2 2 2 0 0 1 4.1 2h3a2 2 0 0 1 2 1.7c.1 1 .4 1.9.7 2.8a2 2 0 0 1-.5 2.1L8 9.9a16 16 0 0 0 6 6l1.3-1.3a2 2 0 0 1 2.1-.4c.9.3 1.8.6 2.8.7a2 2 0 0 1 1.8 2z"/></svg>
        044-987 654 321
      </li>
      <li>
        <svg viewBox="0 0 24 24" fill="none" stroke="#a9a9a9" stroke-width="1.8" stroke-linejoin="round"><rect x="2" y="5" width="20" height="14"/><path d="M2 5l10 8 10-8"/></svg>
        info@marrowfield.com
      </li>
      <li>
        <svg viewBox="0 0 24 24" fill="none" stroke="#a9a9a9" stroke-width="1.6"><circle cx="12" cy="12" r="10"/><ellipse cx="12" cy="12" rx="4.5" ry="10"/><path d="M2 12h20M4 7h16M4 17h16"/></svg>
        www.marrowfield.com
      </li>
    </ul>
    <p class="address">18, Larchmont Avenue 40211, United States</p>
  </section>

  <section class="card card--back">
    <div class="brand"><span class="brand__dot"></span>Marrowfield Benefit Advisors</div>
  </section>
</main>
</body>
</html>
```